New Architectural Firm Business Cards

New Business card to compliment previous pixel forum logo (attached). Please design a business card that is simple, modern, creative....please do not use "symbols", simply the logo and associated graphics/text. The front should contain name/address/phone/email/web address (with graphics).....back should be 100% graphic design using the logo somehow. Hoping for a two color (black and yellow) design. full bleed design, no borders

Target Market(s)

Commercial Architecture Clients

Industry/Entity Type

Architecture

Contact Information for Business Card

Please design a business card that is simple, modern, creative....please do not use "symbols", simply the logo and associated graphics/text. The front should contain name/address/phone/email/web address (with graphics).....back should be 100% graphic design using the logo somehow

Font styles to use
Sans Serif

Colors
FFF300
FFF600
FEFA6F
FFFEC7
FFFEE8

Requirements
Must have
• Clean, Modern Design
Should not have
• Stock images or "icons"

```html
<!DOCTYPE html>
<html lang="en">
<head>
<meta charset="utf-8">
<title>Halvane Architecture – Business Card</title>
<link href="https://fonts.googleapis.com/css2?family=Montserrat:wght@600;700&family=Roboto:wght@400;700&display=swap" rel="stylesheet">
<style>
  :root {
    --backdrop: #bebdbe;
    --card: #ffffff;
    --pattern: #f7f7f7;
    --yellow: #f6c417;
    --ink: #161616;
  }
  * { margin: 0; padding: 0; box-sizing: border-box; }
  html, body { width: 1200px; height: 1200px; overflow: hidden; }
  body { background: var(--backdrop); position: relative; font-family: "Roboto", Arial, sans-serif; color: var(--ink); }

  .card { position: absolute; left: 202px; width: 795px; height: 455px; background: var(--card); }
  .card--cover { top: 112px; }
  .card--contact { top: 645px; }

  .cover-pattern { position: absolute; inset: 0; background: var(--pattern); }

  .wordmark { position: absolute; display: flex; flex-direction: column; align-items: center; font-family: "Roboto", Arial, sans-serif; font-weight: 700; color: var(--yellow); line-height: 1; white-space: nowrap; }
  .wordmark--large { left: 0; right: 0; top: 112px; }
  .wordmark--large .wordmark-name { font-size: 116px; letter-spacing: -2px; }
  .wordmark--large .wordmark-sub { font-size: 40px; margin-top: 22px; letter-spacing: -0.5px; }
  .wordmark--small { left: 28px; top: 26px; width: 140px; }
  .wordmark--small .wordmark-name { font-size: 44px; letter-spacing: -1px; }
  .wordmark--small .wordmark-sub { font-size: 20px; margin-top: 12px; letter-spacing: -0.3px; }

  .person { position: absolute; left: 19px; top: 204px; font-family: "Montserrat", Arial, sans-serif; }
  .person-name { font-size: 29px; font-weight: 700; color: var(--yellow); letter-spacing: 0.5px; line-height: 1; }
  .person-role { font-size: 17px; font-weight: 700; margin-top: 10px; line-height: 1; }

  .divider { position: absolute; left: 19px; top: 284px; width: 760px; height: 1px; background: var(--yellow); }

  .contact-list { position: absolute; left: 19px; top: 301px; list-style: none; }
  .contact-item { display: flex; align-items: center; height: 33px; font-size: 18px; }
  .contact-item svg { width: 20px; height: 20px; margin-right: 19px; flex: none; }

  .address { position: absolute; left: 527px; top: 350px; display: flex; align-items: flex-start; font-size: 18px; line-height: 23px; }
  .address svg { width: 18px; height: 26px; margin-right: 12px; margin-top: 2px; flex: none; }
</style>
</head>
<body>

<section class="card card--cover">
  <div class="cover-pattern" role="img" aria-label="Faint light grey isometric cube line pattern across the card"></div>
  <div class="wordmark wordmark--large">
    <span class="wordmark-name">Halvane</span>
    <span class="wordmark-sub">ARCHITECTURE</span>
  </div>
</section>

<section class="card card--contact">
  <div class="wordmark wordmark--small">
    <span class="wordmark-name">Halvane</span>
    <span class="wordmark-sub">ARCHITECTURE</span>
  </div>

  <div class="person">
    <p class="person-name">ALAN REED</p>
    <p class="person-role">Director</p>
  </div>

  <div class="divider"></div>

  <ul class="contact-list">
    <li class="contact-item">
      <svg viewBox="0 0 20 20" aria-hidden="true"><circle cx="10" cy="10" r="10" fill="#161616"/><path d="M6.5 5.5l2 .2.8 2.2-1.2 1a6 6 0 0 0 3 3l1-1.2 2.2.8.2 2c-4.5.6-8.6-3.5-8-8z" fill="#fff"/></svg>
      <span>555 018 2040</span>
    </li>
    <li class="contact-item">
      <svg viewBox="0 0 20 20" aria-hidden="true"><rect x="1" y="3" width="18" height="14" fill="#161616"/><path d="M4 6l6 5 6-5" stroke="#fff" stroke-width="1.8" fill="none"/></svg>
      <span>hello@halvanestudio.com</span>
    </li>
    <li class="contact-item">
      <svg viewBox="0 0 20 20" aria-hidden="true"><circle cx="10" cy="10" r="9" fill="#161616"/><g stroke="#fff" stroke-width="1" fill="none"><ellipse cx="10" cy="10" rx="4" ry="9"/><path d="M10 1v18M1 10h18M2.5 6h15M2.5 14h15"/></g></svg>
      <span>www.halvanestudio.com</span>
    </li>
  </ul>

  <div class="address">
    <svg viewBox="0 0 18 26" aria-hidden="true"><path d="M9 0a9 9 0 0 0-9 9c0 7 9 17 9 17s9-10 9-17a9 9 0 0 0-9-9z" fill="#161616"/><circle cx="9" cy="9" r="3.4" fill="#fff"/></svg>
    <p>18 Harbour Lane road<br>eastfield bay 4102</p>
  </div>
</section>

</body>
</html>
```